Health care technology software systems

We have a solid logo. We have company colors that will need to be used as well. We just need a great business card design. We sell to health plans but want to be modern
Updates

Need extra days to review

Target Market(s)

Health technology sector selling into Health Plans

Industry/Entity Type

Health Care Technology

Contact Information for Business Card

Name, title, address, phone number, email

Requirements
Must have
• Use of Kembrata corporate colors - Uploaded w/ our logos

```html
<!DOCTYPE html>
<html lang="en">
<head>
<meta charset="utf-8">
<title>Kembrata Business Card</title>
<link href="https://fonts.googleapis.com/css2?family=Montserrat:wght@300;400;700&display=swap" rel="stylesheet">
<style>
  :root {
    --stage: #262626;
    --paper: #ffffff;
    --navy: #3a5dab;
    --sky: #1ea6de;
    --lime: #8cc63f;
    --ink: #2b2b2b;
  }
  * { margin: 0; padding: 0; box-sizing: border-box; }
  html, body {
    width: 1200px; height: 1059px; overflow: hidden;
    background: var(--stage);
    font-family: "Montserrat", Arial, sans-serif;
  }
  .card {
    position: absolute; left: 255px;
    width: 690px; height: 392px;
    border-radius: 22px; overflow: hidden;
  }
  .card--front { top: 89px; background: var(--paper); }
  .card--back { top: 548px; background: var(--navy); }

  .waves { position: absolute; inset: 0; width: 100%; height: 100%; }

  .brand { position: absolute; display: flex; align-items: center; gap: 16px; white-space: nowrap; }
  .brand__dot { width: 46px; height: 46px; border-radius: 50%; flex: none; }
  .brand__name { font-weight: 300; font-size: 50px; line-height: 1; letter-spacing: 0.5px; }

  .card--front .brand { left: 30px; top: 46px; }
  .card--front .brand__dot { background: var(--navy); }
  .card--front .brand__name { color: var(--ink); }

  .card--back .brand { right: 48px; top: 304px; }
  .card--back .brand__dot { background: var(--paper); }
  .card--back .brand__name { color: var(--paper); }

  .person { position: absolute; right: 27px; top: 48px; text-align: right; }
  .person__name { font-weight: 700; font-size: 24px; letter-spacing: 1px; line-height: 1.1; }
  .person__first { color: var(--lime); }
  .person__last { color: var(--sky); }
  .person__title { font-size: 16px; color: var(--ink); margin-top: 4px; }

  .address {
    position: absolute; right: 27px; top: 238px;
    color: var(--paper); font-size: 16px; line-height: 23px; text-align: right; font-style: normal;
  }
  .contact {
    position: absolute; right: 24px; top: 296px;
    list-style: none; color: var(--paper); font-size: 16px; line-height: 22px;
  }
  .contact__item { display: flex; justify-content: flex-end; align-items: center; gap: 7px; }
  .contact__icon { width: 12px; height: 12px; flex: none; }
</style>
</head>
<body>

<section class="card card--front">
  <svg class="waves" viewBox="0 0 690 392" preserveAspectRatio="none" aria-hidden="true">
    <path fill="var(--navy)" d="M0,312 C60,340 160,355 260,330 C380,300 470,180 590,194 C640,198 670,208 690,218 V392 H0 Z"/>
    <path fill="var(--sky)" d="M0,270 C50,295 110,318 170,316 C230,314 290,290 341,263 C290,295 220,332 150,333 C90,334 40,315 0,295 Z"/>
    <path fill="var(--lime)" d="M215,328 C350,280 460,165 585,170 C640,172 670,188 690,200 V212 C660,198 630,186 585,186 C470,186 360,275 215,328 Z"/>
  </svg>

  <div class="brand">
    <span class="brand__dot"></span>
    <span class="brand__name">kembrata</span>
  </div>

  <div class="person">
    <p class="person__name"><span class="person__first">DELAN</span> <span class="person__last">CARVER</span></p>
    <p class="person__title">Owner/CEO</p>
  </div>

  <address class="address">
    1450 Harlow Avenue<br>
    Brenton County 4817
  </address>

  <ul class="contact">
    <li class="contact__item">123-608-37254
      <svg class="contact__icon" viewBox="0 0 12 12"><path fill="var(--sky)" d="M2.5 1 L4.5 1 L5.2 3.5 L4 4.5 C4.6 6 6 7.4 7.5 8 L8.5 6.8 L11 7.5 V9.5 C11 10.3 10.3 11 9.5 11 C5 11 1 7 1 2.5 C1 1.7 1.7 1 2.5 1 Z"/></svg>
    </li>
    <li class="contact__item">info@kembrata.com
      <svg class="contact__icon" viewBox="0 0 12 12"><rect x="0.5" y="2" width="11" height="8" fill="var(--sky)"/><path d="M0.5 2 L6 6.5 L11.5 2" fill="none" stroke="var(--navy)" stroke-width="1"/></svg>
    </li>
    <li class="contact__item">www.kembrata.com
      <svg class="contact__icon" viewBox="0 0 12 12"><circle cx="6" cy="6" r="5.5" fill="var(--sky)"/><path d="M0.5 6 H11.5 M6 0.5 C3.5 3 3.5 9 6 11.5 M6 0.5 C8.5 3 8.5 9 6 11.5" fill="none" stroke="var(--navy)" stroke-width="0.8"/></svg>
    </li>
  </ul>
</section>

<section class="card card--back">
  <div class="brand">
    <span class="brand__dot"></span>
    <span class="brand__name">kembrata</span>
  </div>
</section>

</body>
</html>
```